Radio Service company needs ad for trade publication

Airwave Partners provides sales, content, production, technology, and promotion products and services to radio stations to help increase sales and solutions to improve operations and reduce costs. We are looking for a creative ad (sizes 720x250, 300x250, 728x180) with a theme around "MASTER YOUR 2024 BUDGET with AIRWAVE PARTNERS". Categories we have products/services to help them get budget into alignment. (1) Sales (2) Content & Programming (3) Technology (4) Production & Imaging (5) Promotions & Marketing (6) Support Services
"Don't go into the new year with an Unrealistic Budget.....We can Help!"

```html
<!DOCTYPE html>
<html lang="en">
<head>
<meta charset="UTF-8">
<title>Airwave Partners – Master Your 2024 Budget ads</title>
<link href="https://fonts.googleapis.com/css2?family=Oswald:wght@600;700&family=Poppins:wght@400;600;700&display=swap" rel="stylesheet">
<style>
  :root {
    --page-bg: #1a97ef;
    --navy: #2a3a92;
    --navy-deep: #1c2766;
    --accent: #1b8cf0;
    --white: #ffffff;
    --yellow: #fdc12e;
    --mic-dark: #15161c;
    --mic-mid: #50535c;
  }
  * { box-sizing: border-box; margin: 0; padding: 0; }
  html, body { width: 1067px; height: 1200px; overflow: hidden; }
  body { background: var(--page-bg); position: relative; font-family: "Poppins", sans-serif; }

  .ad {
    position: absolute;
    background: var(--navy);
    overflow: hidden;
    box-shadow: 0 6px 14px rgba(0, 0, 0, 0.35);
    color: var(--white);
  }
  .ad--leaderboard { left: 53px; top: 104px; width: 960px; height: 332px; }
  .ad--wide { left: 49px; top: 480px; width: 970px; height: 239px; }
  .ad--square { left: 49px; top: 763px; width: 447px; height: 372px; }

  .headline { position: absolute; font-family: "Oswald", sans-serif; font-weight: 700; text-transform: uppercase; line-height: 0.9; }
  .headline span { display: block; white-space: nowrap; }
  .headline .mid { position: relative; }
  .headline .with-tag {
    position: absolute; background: var(--accent); color: var(--navy-deep);
    font-family: "Poppins", sans-serif; font-weight: 700; line-height: 1; padding: 2px 5px;
    transform: rotate(-4deg);
  }

  .divider-v { position: absolute; width: 2px; background: var(--white); }
  .divider-h { position: absolute; height: 2px; background: var(--white); }

  .services { position: absolute; }
  .services h2 { font-weight: 700; text-transform: uppercase; white-space: nowrap; }
  .services ul { list-style: none; }
  .services li { position: relative; white-space: nowrap; }
  .services li::before {
    content: ""; position: absolute; left: 0; top: 50%; transform: translateY(-50%);
    border-style: solid; border-color: transparent transparent transparent var(--accent);
  }

  .brand-corner { position: absolute; top: 0; right: 0; }
  .brand-corner svg { position: absolute; inset: 0; width: 100%; height: 100%; }
  .brand-name {
    position: absolute; font-family: "Poppins", sans-serif; font-weight: 700;
    color: var(--accent); text-align: center; line-height: 1; text-transform: uppercase;
  }

  .mic-photo {
    position: absolute;
    background: radial-gradient(ellipse at 35% 40%, var(--mic-mid) 0%, var(--mic-dark) 55%, rgba(21,22,28,0) 72%);
  }

  .help-badge {
    position: absolute; background: var(--yellow); color: var(--navy-deep);
    font-family: "Oswald", sans-serif; font-weight: 700; text-transform: uppercase;
    display: flex; align-items: center; justify-content: center; text-align: center; line-height: 1.2;
    border-radius: 58% 42% 52% 48% / 46% 55% 45% 54%;
  }

  .tagline-strip {
    position: absolute; background: var(--accent); color: var(--navy-deep);
    font-weight: 600; display: flex; align-items: center; justify-content: center; white-space: nowrap;
  }
</style>
</head>
<body>

<!-- 728x250 leaderboard -->
<section class="ad ad--leaderboard">
  <h1 class="headline" style="left:43px;top:20px;">
    <span style="font-size:82px;">Master</span>
    <span class="mid" style="font-size:36px;margin-top:2px;">Your 2024 Budget</span>
    <span style="font-size:76px;margin-top:6px;">Airwave</span>
    <span style="font-size:60px;">Partners</span>
    <em class="with-tag" style="left:118px;top:118px;font-size:14px;font-style:normal;">WITH</em>
  </h1>
  <div class="divider-v" style="left:364px;top:56px;height:173px;"></div>
  <div class="services" style="left:391px;top:32px;">
    <h2 style="font-size:22px;margin-bottom:6px;">Our Products/Services</h2>
    <ul style="font-size:22px;line-height:32px;">
      <li style="padding-left:24px;">Sales</li>
      <li style="padding-left:24px;">Technology</li>
      <li style="padding-left:30px;">Support Services</li>
      <li style="padding-left:24px;">Production &amp; Imaging</li>
      <li style="padding-left:24px;">Promotions &amp; Marketing</li>
      <li style="padding-left:24px;">Content &amp; Programming</li>
    </ul>
  </div>
  <div class="tagline-strip" style="left:56px;top:280px;width:633px;height:30px;font-size:15px;">Don't go into the new year with an Unrealistic Budget.....We can Help!</div>
  <div class="mic-photo" role="img" aria-label="Studio microphone with pop filter" style="left:787px;top:83px;width:173px;height:249px;"></div>
  <div class="brand-corner" style="width:200px;height:110px;">
    <svg viewBox="0 0 200 110" preserveAspectRatio="none" aria-hidden="true"><path d="M0 0H200V110C110 112 30 80 0 0Z" fill="var(--white)"/></svg>
    <div class="brand-name" style="left:55px;top:28px;width:140px;font-size:20px;">Airwave<br>Partners</div>
  </div>
</section>

<!-- 728x180 wide -->
<section class="ad ad--wide">
  <h1 class="headline" style="left:35px;top:16px;">
    <span style="font-size:60px;">Master</span>
    <span class="mid" style="font-size:27px;margin-top:1px;">Your 2024 Budget</span>
    <span style="font-size:55px;margin-top:4px;">Airwave</span>
    <span style="font-size:45px;">Partners</span>
    <em class="with-tag" style="left:96px;top:86px;font-size:11px;font-style:normal;">WITH</em>
  </h1>
  <div class="divider-v" style="left:300px;top:47px;height:146px;"></div>
  <div class="services" style="left:324px;top:27px;">
    <h2 style="font-size:18px;margin-bottom:2px;">Our Products/Services</h2>
    <ul style="font-size:18px;line-height:27px;">
      <li style="padding-left:20px;">Sales</li>
      <li style="padding-left:20px;">Technology</li>
      <li style="padding-left:26px;">Support Services</li>
      <li style="padding-left:20px;">Production &amp; Imaging</li>
      <li style="padding-left:20px;">Promotions &amp; Marketing</li>
      <li style="padding-left:20px;">Content &amp; Programming</li>
    </ul>
  </div>
  <div class="mic-photo" role="img" aria-label="Studio microphone with pop filter" style="left:624px;top:13px;width:233px;height:226px;"></div>
  <div class="brand-corner" style="width:195px;height:110px;">
    <svg viewBox="0 0 200 110" preserveAspectRatio="none" aria-hidden="true"><path d="M0 0H200V110C110 112 30 80 0 0Z" fill="var(--white)"/></svg>
    <div class="brand-name" style="left:52px;top:26px;width:140px;font-size:20px;">Airwave<br>Partners</div>
  </div>
  <div class="help-badge" style="left:791px;top:103px;width:140px;height:107px;font-size:27px;">We Can<br>Help</div>
</section>

<!-- 300x250 square -->
<section class="ad ad--square">
  <h1 class="headline" style="left:27px;top:18px;">
    <span style="font-size:56px;">Master</span>
    <span class="mid" style="font-size:24px;margin-top:1px;">Your 2024 Budget</span>
    <span style="font-size:52px;margin-top:4px;">Airwave</span>
    <span style="font-size:40px;">Partners</span>
    <em class="with-tag" style="left:84px;top:80px;font-size:10px;font-style:normal;">WITH</em>
  </h1>
  <div class="divider-h" style="left:31px;top:206px;width:190px;"></div>
  <div class="services" style="left:27px;top:217px;">
    <h2 style="font-size:14px;margin-bottom:1px;">Our Products/Services</h2>
    <ul style="font-size:14px;line-height:20.5px;">
      <li style="padding-left:16px;">Sales</li>
      <li style="padding-left:16px;">Technology</li>
      <li style="padding-left:20px;">Support Services</li>
      <li style="padding-left:16px;">Production &amp; Imaging</li>
      <li style="padding-left:16px;">Promotions &amp; Marketing</li>
      <li style="padding-left:16px;">Content &amp; Programming</li>
    </ul>
  </div>
  <div class="mic-photo" role="img" aria-label="Studio microphone with pop filter" style="left:291px;top:111px;width:156px;height:261px;"></div>
  <div class="brand-corner" style="width:196px;height:113px;">
    <svg viewBox="0 0 200 110" preserveAspectRatio="none" aria-hidden="true"><path d="M0 0H200V110C110 112 30 80 0 0Z" fill="var(--white)"/></svg>
    <div class="brand-name" style="left:54px;top:26px;width:140px;font-size:19px;">Airwave<br>Partners</div>
  </div>
  <div class="help-badge" style="left:227px;top:257px;width:113px;height:104px;font-size:22px;">We Can<br>Help</div>
</section>

<style>
  .ad--leaderboard .services li::before { border-width: 8px 0 8px 11px; }
  .ad--wide .services li::before { border-width: 7px 0 7px 9px; }
  .ad--square .services li::before { border-width: 5px 0 5px 7px; }
</style>
</body>
</html>
```